Software Company Business Card

We are looking for a new design of our business card. The design will also be used in the rest of our branding and marketing materials as we want to keep it all uniform. We sell POS software to fine/luxury jewelers and also offer other business services as well to help the jeweler manage their business and need something more updated, technical and fresh, preferably more on the masculine side. We do not want any designs with gems in them but if possible would like to incorporate the circle and arrow in the logo into the design, but not a requirement if you can't make it work. I would like to see a variety of the mix. The colors need to remain our blue and orange and the logo can not change. The squiggly lines have been used as our corporate identity for over 20 years and its time to update. Our company name is PELK (Bright Ledger Counter Solutions).

Target Market(s)

High End Jewelers

Industry/Entity Type

Software

Contact Information for Business Card

Requirements
Must have
• Our logo and the colors must remain the same. Blue is #d95d39 and Orange is #0f5682.
Nice to have
• The circle and arrow incorporated but not a requirement.
Should not have
• Anything jewelry or gem related.

```html
<!DOCTYPE html>
<html lang="en">
<head>
<meta charset="utf-8">
<title>PELK Business Card</title>
<link href="https://fonts.googleapis.com/css2?family=Montserrat:wght@400;700;800&display=swap" rel="stylesheet">
<style>
  :root {
    --backdrop: #0a4e7f;
    --brand-blue: #0f5682;
    --brand-orange: #d95d39;
    --card: #ffffff;
    --text-grey: #555555;
    --rule: #9a9a9a;
  }
  * { margin: 0; padding: 0; box-sizing: border-box; }
  html, body { width: 1111px; height: 1200px; overflow: hidden; }
  body {
    position: relative;
    background: var(--backdrop);
    font-family: "Montserrat", Arial, sans-serif;
  }
  .card {
    position: absolute;
    left: 123px;
    width: 859px;
    height: 491px;
    background: var(--card);
    box-shadow: 8px 10px 18px rgba(0, 20, 40, 0.35);
  }
  .card--front { top: 58px; }
  .card--back { top: 608px; }

  .brand-name {
    position: absolute;
    font-weight: 800;
    font-size: 66px;
    line-height: 1;
    letter-spacing: 4px;
    color: var(--brand-blue);
  }
  .brand-dot {
    position: absolute;
    width: 62px;
    height: 62px;
    border-radius: 50%;
    background: var(--brand-orange);
  }
  .card--front .brand-name { left: 58px; top: 212px; }
  .card--front .brand-dot { left: 280px; top: 213px; }
  .card--back .brand-name { left: 282px; top: 214px; }
  .card--back .brand-dot { left: 519px; top: 214px; width: 64px; height: 64px; }

  .divider {
    position: absolute;
    left: 392px;
    top: 139px;
    width: 1px;
    height: 193px;
    background: var(--rule);
  }
  .person-name {
    position: absolute;
    left: 440px;
    top: 112px;
    font-weight: 700;
    font-size: 38px;
    line-height: 1.2;
    color: var(--brand-blue);
    white-space: nowrap;
  }
  .person-title {
    position: absolute;
    left: 440px;
    top: 160px;
    font-weight: 400;
    font-size: 18px;
    color: var(--brand-orange);
    white-space: nowrap;
  }
  .contact-list {
    position: absolute;
    left: 440px;
    top: 209px;
    list-style: none;
  }
  .contact-item {
    display: flex;
    align-items: flex-start;
    font-size: 19px;
    line-height: 23px;
    color: var(--text-grey);
    margin-bottom: 5px;
    white-space: nowrap;
  }
  .contact-item:nth-child(3) { margin-bottom: 5px; }
  .contact-icon {
    width: 14px;
    height: 14px;
    margin: 5px 30px 0 3px;
    flex: none;
    fill: var(--brand-orange);
  }
  .contact-icon--pin { width: 14px; height: 20px; margin-top: 6px; }
</style>
</head>
<body>
  <section class="card card--front">
    <div class="brand-name">PELK</div>
    <div class="brand-dot"></div>
    <div class="divider"></div>
    <h1 class="person-name">Dorian Halvers</h1>
    <p class="person-title">Director of Global Operation</p>
    <ul class="contact-list">
      <li class="contact-item">
        <svg class="contact-icon" viewBox="0 0 24 24" aria-hidden="true"><path d="M6.6 10.8c1.4 2.8 3.8 5.1 6.6 6.6l2.2-2.2c.3-.3.7-.4 1-.2 1.1.4 2.3.6 3.6.6.6 0 1 .4 1 1V20c0 .6-.4 1-1 1C10.6 21 3 13.4 3 4c0-.6.4-1 1-1h3.5c.6 0 1 .4 1 1 0 1.3.2 2.5.6 3.6.1.3 0 .7-.2 1z"/></svg>
        <span>+1 800 555 0147</span>
      </li>
      <li class="contact-item">
        <svg class="contact-icon" viewBox="0 0 24 24" aria-hidden="true"><path d="M2 8h4v14H2zM8 4h10l4 4v14H8zm3 7v3h3v-3zm5 0v3h3v-3zm-5 5v3h3v-3zm5 0v3h3v-3z"/></svg>
        <span>+1 703 555 0182</span>
      </li>
      <li class="contact-item">
        <svg class="contact-icon" viewBox="0 0 24 24" aria-hidden="true"><path d="M12 2a10 10 0 1 0 5 18.7l-1-1.7A8 8 0 1 1 20 12v1.5a1.5 1.5 0 0 1-3 0V12a5 5 0 1 0-1.5 3.5A3.5 3.5 0 0 0 22 13.5V12A10 10 0 0 0 12 2zm0 13a3 3 0 1 1 0-6 3 3 0 0 1 0 6z"/></svg>
        <span>dorian@pelkusa.com</span>
      </li>
      <li class="contact-item">
        <svg class="contact-icon" viewBox="0 0 24 24" aria-hidden="true"><path d="M12 2a10 10 0 1 0 0 20 10 10 0 0 0 0-20zm6.9 6h-3a15 15 0 0 0-1.3-3.9A8 8 0 0 1 18.9 8zM12 4c.8 1.2 1.5 2.5 1.9 4h-3.8c.4-1.5 1.1-2.8 1.9-4zM4.3 14a8 8 0 0 1 0-4h3.4a16 16 0 0 0 0 4zm.8 2h3a15 15 0 0 0 1.3 3.9A8 8 0 0 1 5.1 16zm3-8h-3a8 8 0 0 1 4.3-3.9C8.8 5.3 8.4 6.6 8.1 8zM12 20c-.8-1.2-1.5-2.5-1.9-4h3.8c-.4 1.5-1.1 2.8-1.9 4zm2.3-6H9.7a14 14 0 0 1 0-4h4.6a14 14 0 0 1 0 4zm.3 5.9c.6-1.2 1-2.5 1.3-3.9h3a8 8 0 0 1-4.3 3.9zM16.3 14a16 16 0 0 0 0-4h3.4a8 8 0 0 1 0 4z"/></svg>
        <span>www.pelkusa.com</span>
      </li>
      <li class="contact-item">
        <svg class="contact-icon contact-icon--pin" viewBox="0 0 16 24" aria-hidden="true"><path d="M8 0a8 8 0 0 0-8 8c0 6 8 16 8 16s8-10 8-16a8 8 0 0 0-8-8zm0 10.5a2.5 2.5 0 1 1 0-5 2.5 2.5 0 0 1 0 5z"/></svg>
        <span>1480 Meridian Circle Suite 212<br>Carlow, NV 89011 USA</span>
      </li>
    </ul>
  </section>

  <section class="card card--back">
    <div class="brand-name">PELK</div>
    <div class="brand-dot"></div>
  </section>
</body>
</html>
```